New Business Card

We need to refresh our business cards. We designed these ourselves and we have no graphic design experience. We would like to find a new business card design that is professional and unique. We are an auto finance company. Feel free to play with the logo, but we would like to keep the eye very present on the card. Our corporate colors are green, grey, and white.
Green - RGB - 168,215,27; HEX - #AADD22
Grey - RGB - 196,196,196; HEX - #C4C4C4
Updates
Need to upload the vector file to finalize the project. The last logo was for a jpeg that didn't stretch well.
Industry/Entity Type
Financial Service
Contact Information for Business Card
Honestly don't know...I need your help!

```html
<!DOCTYPE html>
<html lang="en">
<head>
<meta charset="utf-8">
<title>Farview Capital – Business Card</title>
<link href="https://fonts.googleapis.com/css2?family=Lato:wght@400;700;900&display=swap" rel="stylesheet">
<style>
  :root {
    --page: #fdfdfb;
    --card-grey: #7a7a7a;
    --brand-green: #a8d71b;
    --white: #ffffff;
    --soft-grey: #c4c4c4;
  }
  * { margin: 0; padding: 0; box-sizing: border-box; }
  html, body {
    width: 1200px; height: 1000px; overflow: hidden;
    background: var(--page);
    font-family: "Lato", Arial, sans-serif;
  }
  .canvas { position: relative; width: 1200px; height: 1000px; }

  .card-face {
    position: absolute; left: 192px; width: 831px;
    background: var(--card-grey);
  }
  .card-face--front { top: 2px; height: 432px; }
  .card-face--back { top: 505px; height: 430px; }

  .web-band {
    position: absolute; left: 192px; width: 831px; height: 58px;
    background: var(--brand-green);
    color: var(--white);
    font-weight: 700; font-size: 17px;
    text-align: center; padding-top: 6px;
  }
  .web-band--front { top: 442px; }
  .web-band--back { top: 943px; }

  /* Front brand lockup */
  .brand-front {
    position: absolute; left: 0; right: 0; top: 150px;
    display: flex; flex-direction: column; align-items: center;
  }
  .brand-dot {
    width: 92px; height: 92px; border-radius: 50%;
    background: var(--brand-green);
  }
  .brand-name {
    margin-top: 28px;
    color: var(--brand-green);
    font-weight: 700; font-size: 46px; letter-spacing: 0.5px;
    line-height: 1;
  }

  /* Back brand lockup */
  .brand-back {
    position: absolute; left: 54px; top: 205px;
    display: flex; align-items: center; gap: 20px;
  }
  .brand-back .brand-dot { width: 70px; height: 70px; }
  .brand-back .brand-name { margin-top: 0; font-size: 40px; }

  .divider {
    position: absolute; left: 475px; top: 148px;
    width: 6px; height: 197px; background: var(--white);
    border-right: 2px solid var(--brand-green);
  }

  .contact-block {
    position: absolute; left: 496px; top: 140px; color: var(--white);
  }
  .person-name { font-weight: 400; font-size: 29px; line-height: 1.1; }
  .person-name .first { color: var(--brand-green); font-weight: 900; }
  .person-role { font-weight: 700; font-size: 18px; margin-top: 3px; }
  .person-role .muted { color: var(--soft-grey); }

  .contact-list { list-style: none; margin-top: 23px; font-weight: 700; font-size: 17px; }
  .contact-list li { display: flex; align-items: flex-start; line-height: 22px; }
  .contact-list .icon { width: 16px; height: 22px; margin-right: 14px; flex: none; }
</style>
</head>
<body>
<div class="canvas">

  <section class="card-face card-face--front">
    <div class="brand-front">
      <div class="brand-dot"></div>
      <div class="brand-name">Farview Capital</div>
    </div>
  </section>
  <div class="web-band web-band--front">www.farviewcapital.cam</div>

  <section class="card-face card-face--back">
    <div class="brand-back">
      <div class="brand-dot"></div>
      <div class="brand-name">Farview Capital</div>
    </div>

    <div class="divider"></div>

    <div class="contact-block">
      <div class="person-name"><span class="first">Rowan</span> Pellard</div>
      <div class="person-role">Financial <span class="muted">Director</span></div>
      <ul class="contact-list">
        <li>
          <svg class="icon" viewBox="0 0 16 22"><rect x="1" y="7" width="14" height="10" fill="#a8d71b"/><path d="M1 7 L8 13 L15 7" stroke="#7a7a7a" stroke-width="1.4" fill="none"/></svg>
          farview@mailbox.com
        </li>
        <li>
          <svg class="icon" viewBox="0 0 16 22"><rect x="4" y="4" width="8" height="14" rx="1.5" fill="none" stroke="#fff" stroke-width="1.6"/><rect x="7" y="15" width="2" height="1.5" fill="#fff"/></svg>
          555.014.2290
        </li>
        <li>
          <svg class="icon" viewBox="0 0 16 22"><path d="M1 10 Q8 4 15 10 L13 12 L11 10 L5 10 L3 12 Z" fill="#a8d71b"/><rect x="3" y="12" width="10" height="5" rx="1" fill="#a8d71b"/></svg>
          555.014.2290
        </li>
        <li>
          <svg class="icon" viewBox="0 0 16 22"><path d="M8 4 a4.5 4.5 0 0 1 4.5 4.5 C12.5 12 8 17 8 17 C8 17 3.5 12 3.5 8.5 A4.5 4.5 0 0 1 8 4 Z" fill="#fff"/><circle cx="8" cy="8.5" r="1.7" fill="#7a7a7a"/></svg>
          <span>21470 - your street<br>Your country. K2P 4R8</span>
        </li>
      </ul>
    </div>
  </section>
  <div class="web-band web-band--back">www.farviewcapital.cam</div>

</div>
</body>
</html>
```